Business Card Design

We need a business card to highlight our property maintenance company. we specialize in commercial and industrial property maintenance. services include landscaping snow and ice management. janitorial services. cleanroom services. parking lot maintenance.
Updates
I have narrowed down to two designs thank you waiting on some minor changes to both designs to choose.
Target Market(s)
facility managers/property managers
Industry/Entity Type
Property Maintenance
Contact Information for Business Card
27 Wendlow Rd.
Halden, MA. 01892
978-552-0371
Look and feel

```html
<!DOCTYPE html>
<html lang="en">
<head>
<meta charset="utf-8">
<title>Meridian Facilities Services – Business Card</title>
<link rel="stylesheet" href="https://fonts.googleapis.com/css2?family=Cinzel:wght@600;700&family=Montserrat:wght@800&family=Roboto:wght@400;500&display=swap">
<style>
  :root {
    --canvas: #e8e5e1;
    --card-dark: #15191d;
    --card-dark-2: #1f252b;
    --accent-blue: #2ba3e0;
    --brand-yellow: #f3c417;
    --white: #ffffff;
  }
  * { margin: 0; padding: 0; box-sizing: border-box; }
  html, body { width: 1200px; height: 800px; overflow: hidden; }
  body { background: var(--canvas); position: relative; }

  .card {
    position: absolute;
    border-radius: 4px;
    overflow: hidden;
    box-shadow: 0 10px 24px rgba(0,0,0,0.25);
  }
  .card-back {
    left: 90px;
    top: 130px;
    width: 309px;
    height: 540px;
    background: linear-gradient(135deg, var(--card-dark-2), var(--card-dark));
  }
  .card-front {
    left: 450px;
    top: 245px;
    width: 540px;
    height: 309px;
  }

  .back-brand {
    position: absolute;
    left: 154px;
    top: 400px;
    width: 300px;
    transform: translate(-50%, -50%) rotate(90deg);
    transform-origin: center;
  }
  .back-brand .brand-name {
    font-family: "Montserrat", sans-serif;
    font-weight: 800;
    font-size: 46px;
    color: var(--accent-blue);
    line-height: 1;
    letter-spacing: 1px;
  }
  .back-brand .tagline {
    font-family: "Cinzel", serif;
    font-weight: 600;
    font-size: 19px;
    color: var(--white);
    line-height: 1.25;
    margin-top: 8px;
  }
  .back-brand .tagline span { display: block; }
  .back-brand .tagline .city { padding-left: 22px; }

  .card-front svg { display: block; }
  .brand-text { font-family: "Montserrat", sans-serif; font-weight: 800; }
  .headline { font-family: "Cinzel", serif; font-weight: 700; }
  .contact { font-family: "Roboto", sans-serif; }
</style>
</head>
<body>

  <section class="card card-back" aria-label="Business card back">
    <div class="back-brand">
      <div class="brand-name">meridian</div>
      <div class="tagline">
        <span>Facilities Services</span>
        <span class="city">Halden, MA</span>
      </div>
    </div>
  </section>

  <section class="card card-front" aria-label="Business card front">
    <svg width="540" height="309" viewBox="0 0 540 309" xmlns="http://www.w3.org/2000/svg">
      <defs>
        <linearGradient id="front-blue" x1="0" y1="0" x2="1" y2="1">
          <stop offset="0" stop-color="#3bb3ef"/>
          <stop offset="1" stop-color="#0d5fb3"/>
        </linearGradient>
      </defs>

      <rect class="base-panel" width="540" height="309" fill="#1a1f24"/>
      <polygon class="header-panel" points="0,0 540,0 540,205 0,88" fill="url(#front-blue)"/>
      <polygon class="divider-band" points="0,88 540,205 540,222 0,105" fill="#3a2f86"/>

      <circle class="brand-dot" cx="40" cy="38" r="11" fill="#f3c417"/>
      <text class="brand-text" x="58" y="47" font-size="26" fill="#f3c417">meridian</text>

      <text class="headline" x="250" y="62" font-size="24" fill="#0c1a2e">Facilities Services</text>
      <text class="headline" x="340" y="94" font-size="24" fill="#0c1a2e">Halden, MA</text>

      <text class="contact" x="22" y="138" font-size="19" font-weight="500" fill="#2ba3e0" letter-spacing="0.5">DANIEL BROOKS</text>
      <text class="contact" x="22" y="156" font-size="11" fill="#d7dbe0">Director</text>

      <g class="contact-row">
        <rect x="22" y="168" width="13" height="13" rx="2" fill="#2ba3e0"/>
        <path d="M26 171 q-1 4 3 7 l1.5 -1.5 l1.8 1.4 l-1.2 1.6 q-6 -1 -7 -7 z" fill="#15191d"/>
        <text class="contact" x="42" y="179" font-size="12" fill="#ffffff">978-552-0371</text>
      </g>
      <g class="contact-row">
        <rect x="22" y="188" width="13" height="13" rx="2" fill="#2ba3e0"/>
        <circle cx="28.5" cy="194.5" r="4" fill="none" stroke="#15191d" stroke-width="1.2"/>
        <line x1="24.5" y1="194.5" x2="32.5" y2="194.5" stroke="#15191d" stroke-width="1"/>
        <text class="contact" x="42" y="199" font-size="12" fill="#ffffff">www.meridianfs.com</text>
      </g>
      <g class="contact-row">
        <rect x="22" y="208" width="13" height="13" rx="2" fill="#2ba3e0"/>
        <path d="M28.5 218.5 l-3 -4 a3 3 0 1 1 6 0 z" fill="#15191d"/>
        <text class="contact" x="42" y="219" font-size="12" fill="#ffffff">27 Wendlow Rd. Halden, Ma. 01892</text>
      </g>

      <g class="service-hex" role="img" aria-label="Photo of janitorial window cleaning">
        <polygon points="452,140 488,161 488,203 452,224 416,203 416,161" fill="#9cc3d6" stroke="#2ba3e0" stroke-width="4"/>
      </g>
      <g class="service-hex" role="img" aria-label="Photo of landscaping tractor on lawn">
        <polygon points="413,208 449,229 449,271 413,292 377,271 377,229" fill="#6f8f4a" stroke="#2ba3e0" stroke-width="4"/>
      </g>
      <g class="service-hex" role="img" aria-label="Photo of snow plow loader in winter lot">
        <polygon points="491,208 527,229 527,271 491,292 455,271 455,229" fill="#7d8287" stroke="#2ba3e0" stroke-width="4"/>
      </g>
    </svg>
  </section>

</body>
</html>
```